Designing a billboard

Should have
Corwell & Pine, LLC
Ph: 512-647-3918
Auto Accidents / Personal Injury
Family Law
Criminal Defense
Real Estate
Free Consultation

Target Market(s)

Legal

Industry/Entity Type

Legal

Font styles to use
Serif
Sans Serif

Requirements
Must have
• Designing a billboard

Should have
Corwell & Pine, LLC
Ph: 512-647-3918
Family Law
Criminal Defense
Real Estate
Free Consultation
Nice to have
• Nice to have info above
Should not have
• None

```html
<!DOCTYPE html>
<html lang="en">
<head>
<meta charset="utf-8">
<title>Corwell &amp; Pine, LLC — Billboard</title>
<link rel="stylesheet" href="https://fonts.googleapis.com/css2?family=Bebas+Neue&family=Cinzel:wght@700;900&family=Oswald:wght@300;700&display=swap">
<style>
  :root {
    --navy: #003264;
    --sky: #0d8ad6;
    --ink: #04080f;
    --deep: #0b2452;
    --white: #ffffff;
  }
  * { margin: 0; padding: 0; box-sizing: border-box; }
  html, body { width: 1200px; height: 1200px; overflow: hidden; background: var(--white); }
  .billboard { position: relative; width: 1200px; height: 1200px; overflow: hidden; background: var(--white); }

  .firm-name {
    position: absolute; top: 60px; left: 0; width: 100%;
    text-align: center; color: var(--navy);
    font-family: "Cinzel", serif; font-weight: 900;
    font-size: 168px; line-height: 160px; letter-spacing: 2px;
  }

  .photo-backdrop {
    position: absolute; inset: 0;
    background:
      radial-gradient(ellipse 55% 45% at 42% 62%, #1a3f7e 0%, var(--deep) 45%, transparent 80%),
      linear-gradient(180deg, #06101f 0%, var(--ink) 100%);
    clip-path: path("M0,448 Q600,572 1200,388 L1200,1200 L0,1200 Z");
  }
  .swoosh { position: absolute; inset: 0; }

  .services {
    position: absolute; top: 538px; left: 0; width: 100%;
    font-family: "Bebas Neue", sans-serif; color: var(--white);
    font-size: 90px; line-height: 101px;
  }
  .service-row { display: flex; justify-content: center; align-items: center; gap: 30px; }
  .service { display: flex; align-items: center; gap: 6px; }
  .tick { width: 64px; height: 56px; flex: none; }

  .divider {
    position: absolute; top: 872px; left: 266px; width: 668px; height: 4px;
    background: var(--white); border-radius: 2px;
  }
  .cta {
    position: absolute; top: 912px; left: 0; width: 100%;
    text-align: center; color: var(--white);
    font-family: "Oswald", sans-serif; font-weight: 300;
    font-size: 56px; line-height: 66px; letter-spacing: 1px;
  }
  .cta strong { font-weight: 700; }
  .phone {
    position: absolute; top: 990px; left: 0; width: 100%;
    text-align: center; color: var(--white);
    font-family: "Bebas Neue", sans-serif;
    font-size: 212px; line-height: 200px; letter-spacing: -2px;
  }
</style>
</head>
<body>
<main class="billboard">
  <h1 class="firm-name">Corwell &amp;<br>Pine, LLC</h1>

  <div class="photo-backdrop" role="img" aria-label="Dark blue-toned photograph of a handshake"></div>

  <svg class="swoosh" viewBox="0 0 1200 1200" aria-hidden="true">
    <path d="M0,403 Q600,510 1200,385 L1200,388 Q600,572 0,448 Z" fill="var(--sky)"/>
  </svg>

  <section class="services">
    <div class="service-row">
      <span class="service">
        <svg class="tick" viewBox="0 0 64 56"><path d="M4,34 L20,50 L60,6" fill="none" stroke="var(--sky)" stroke-width="6" stroke-linecap="round" stroke-linejoin="round"/></svg>
        Auto Accidents / Personal Injury
      </span>
    </div>
    <div class="service-row">
      <span class="service">
        <svg class="tick" viewBox="0 0 64 56"><path d="M4,34 L20,50 L60,6" fill="none" stroke="var(--sky)" stroke-width="6" stroke-linecap="round" stroke-linejoin="round"/></svg>
        Family Law
      </span>
      <span class="service">
        <svg class="tick" viewBox="0 0 64 56"><path d="M4,34 L20,50 L60,6" fill="none" stroke="var(--sky)" stroke-width="6" stroke-linecap="round" stroke-linejoin="round"/></svg>
        Criminal Defense
      </span>
    </div>
    <div class="service-row">
      <span class="service">
        <svg class="tick" viewBox="0 0 64 56"><path d="M4,34 L20,50 L60,6" fill="none" stroke="var(--sky)" stroke-width="6" stroke-linecap="round" stroke-linejoin="round"/></svg>
        Real Estate
      </span>
    </div>
  </section>

  <div class="divider"></div>

  <p class="cta">FOR <strong>FREE CONSULTATION</strong> CALL US AT</p>
  <p class="phone">512-647-3918</p>
</main>
</body>
</html>
```